Assisted living facility needs a business card design

We need a business card design for an assisted living facility in Los Angeles. We have a logo selected but we would like a business card design that will leave a lasting impression on families looking to place their elderly loved ones in our care as well as on other facility providers who may refer their elderly residents to our facility.

```html
<!DOCTYPE html>
<html lang="en">
<head>
<meta charset="utf-8">
<title>Harborview Gardens Senior Living – Business Card</title>
<link rel="stylesheet" href="https://fonts.googleapis.com/css2?family=PT+Serif:wght@400;700&display=swap">
<style>
  :root {
    --canvas-bg: #2e2f31;
    --card-white: #ffffff;
    --card-shade: #e6e7ea;
    --edge-blue: #b4c4ea;
    --brand-blue: #1a6db8;
    --text-grey: #4d4f53;
    --rule-grey: #9a9ca0;
  }
  * { margin: 0; padding: 0; box-sizing: border-box; }
  html, body { width: 1200px; height: 900px; overflow: hidden; }
  body {
    background: var(--canvas-bg);
    font-family: "PT Serif", Georgia, serif;
    position: relative;
  }
  .card {
    position: absolute;
    left: 290px;
    width: 620px;
    height: 354px;
    border-radius: 34px;
    overflow: hidden;
  }
  .card--front {
    top: 80px;
    background: radial-gradient(ellipse 70% 75% at 55% 48%, var(--card-white) 0%, #eef0f5 45%, var(--edge-blue) 100%);
  }
  .card--back {
    top: 466px;
    background: linear-gradient(120deg, var(--card-shade) 0%, var(--card-white) 55%, #f4f4f6 100%);
  }
  .wordmark {
    color: var(--brand-blue);
    font-weight: 400;
    text-align: center;
    line-height: 1.1;
    letter-spacing: 0.06em;
    text-transform: uppercase;
  }
  .card--front .wordmark {
    position: absolute;
    left: 0; right: 0; top: 138px;
    font-size: 34px;
  }
  .wordmark small {
    display: block;
    font-size: 0.38em;
    letter-spacing: 0.5em;
    margin-top: 8px;
  }
  .card--back .wordmark {
    position: absolute;
    left: 36px; top: 38px;
    font-size: 25px;
    text-align: left;
  }
  .holder {
    position: absolute;
    right: 322px; top: 228px;
    text-align: right;
  }
  .holder__role { color: var(--text-grey); font-size: 16px; }
  .holder__name { color: var(--brand-blue); font-size: 20px; font-weight: 700; }
  .divider {
    position: absolute;
    left: 314px; top: 200px;
    width: 1px; height: 110px;
    background: var(--rule-grey);
  }
  .contacts {
    position: absolute;
    left: 330px; top: 200px;
    list-style: none;
  }
  .contacts li {
    display: flex; align-items: center; gap: 10px;
    color: var(--text-grey);
    font-size: 15px;
    height: 27px;
  }
  .contacts svg { width: 15px; height: 15px; fill: var(--brand-blue); flex: none; }
</style>
</head>
<body>
  <section class="card card--front" aria-label="Card front">
    <p class="wordmark">Harborview Gardens<small>Senior Living</small></p>
  </section>

  <section class="card card--back" aria-label="Card back">
    <p class="wordmark">Harborview Gardens<small>Senior Living</small></p>

    <div class="holder">
      <p class="holder__role">Director</p>
      <p class="holder__name">JOHN SMITH</p>
    </div>

    <span class="divider"></span>

    <ul class="contacts">
      <li>
        <svg viewBox="0 0 24 24" aria-hidden="true"><path d="M6.6 10.8a15 15 0 0 0 6.6 6.6l2.2-2.2a1 1 0 0 1 1-.25 11.4 11.4 0 0 0 3.6.57 1 1 0 0 1 1 1V20a1 1 0 0 1-1 1A17 17 0 0 1 3 4a1 1 0 0 1 1-1h3.5a1 1 0 0 1 1 1c0 1.25.2 2.45.57 3.57a1 1 0 0 1-.25 1z"/></svg>
        300-200-9000
      </li>
      <li>
        <svg viewBox="0 0 24 24" aria-hidden="true"><path d="M2 5h20v14H2zm2 2v.5l8 5 8-5V7zm0 3v7h16v-7l-8 5z"/></svg>
        info@harborviewgardens.com
      </li>
      <li>
        <svg viewBox="0 0 24 24" aria-hidden="true"><path d="M12 2a10 10 0 1 0 0 20 10 10 0 0 0 0-20zm6.9 6h-3a15 15 0 0 0-1.3-3.9A8 8 0 0 1 18.9 8zM12 4c.8 1.2 1.5 2.5 1.9 4h-3.8c.4-1.5 1.1-2.8 1.9-4zM4.3 14a8 8 0 0 1 0-4h3.4a16 16 0 0 0 0 4zm.8 2h3a15 15 0 0 0 1.3 3.9A8 8 0 0 1 5.1 16zm3-8h-3a8 8 0 0 1 4.3-3.9A15 15 0 0 0 8.1 8zM12 20c-.8-1.2-1.5-2.5-1.9-4h3.8c-.4 1.5-1.1 2.8-1.9 4zm2.3-6H9.7a14 14 0 0 1 0-4h4.6a14 14 0 0 1 0 4zm.3 5.9a15 15 0 0 0 1.3-3.9h3a8 8 0 0 1-4.3 3.9zM16.3 14a16 16 0 0 0 0-4h3.4a8 8 0 0 1 0 4z"/></svg>
        www.harborviewgardens.com
      </li>
      <li>
        <svg viewBox="0 0 24 24" aria-hidden="true"><path d="M12 2a7 7 0 0 0-7 7c0 5.2 7 13 7 13s7-7.8 7-13a7 7 0 0 0-7-7zm0 9.5A2.5 2.5 0 1 1 12 6.5a2.5 2.5 0 0 1 0 5z"/></svg>
        00 dummy city, dummy place 0000
      </li>
    </ul>
  </section>
</body>
</html>
```